Masculine, visually appealing sales presentation for CPA firm

I have a basic power point that I use for sales presentations and I would like it to be updated to be more appealing and modern.

This is a presentation I give to real estate agents to help them close sales, save taxes, and resolve tax disputes. I would like the powerpoint to be updated to be more visually appealing. I have included the current powerpoint along with some of my logo files.

You don't have to use any of the pictures/clip art that is in the current power point. I only care that the words of the powerpoint make it to the new version.

Target Market(s)

Realtors, Real Estate Agents

Industry/Entity Type

Accounting

Requirements
Must have
• Visually appealing. I don't want it to look like I just took a template and made a normal powerpoint out of it. It should look custom.
Should not have
• Anything unprofessional, anything inconsistent with my brand

```html
<!DOCTYPE html>
<html lang="en">
<head>
<meta charset="utf-8">
<title>Taxation for Real Estate Professionals – Slides</title>
<link rel="stylesheet" href="https://fonts.googleapis.com/css2?family=Arimo:wght@400;700&display=swap">
<style>
  :root {
    --stage: #a09f9f;
    --navy: #0a3a7a;
    --navy-deep: #01163a;
    --navy-bright: #1d6cc4;
    --footer-navy: #04306a;
    --brown: #3a1a06;
    --cream: #fcf3eb;
    --ink-blue: #0f3a73;
    --ink-dark: #1d2a3d;
    --white: #ffffff;
    --photo-tone: #4f6247;
  }
  * { box-sizing: border-box; margin: 0; padding: 0; }
  html, body { width: 1200px; height: 1036px; overflow: hidden; }
  body {
    background: var(--stage);
    font-family: "Arimo", Arial, sans-serif;
    position: relative;
  }
  .slide {
    position: absolute;
    width: 606px;
    height: 455px;
    background: var(--cream);
    overflow: hidden;
  }
  .slide--title { left: 49px; top: 21px; }
  .slide--intro { left: 513px; top: 532px; }

  .header-art {
    position: absolute; left: 0; top: 0; width: 100%;
    background:
      radial-gradient(ellipse 60% 90% at 80% 10%, rgba(70,150,230,.55), transparent 70%),
      radial-gradient(ellipse 40% 120% at 20% 100%, rgba(90,160,220,.35), transparent 70%),
      linear-gradient(180deg, var(--navy) 0%, #06408a 100%);
  }
  .slide--title .header-art { height: 128px; }
  .slide--intro .header-art { height: 77px; }

  .rule { position: absolute; left: 0; width: 100%; background: var(--brown); }

  /* title slide */
  .slide--title .rule--top { top: 116px; height: 9px; }
  .slide--title .rule--bottom { top: 294px; height: 9px; }
  .brand {
    position: absolute; left: 16px; top: 170px;
    display: flex; align-items: center; gap: 8px;
  }
  .brand__dot { width: 26px; height: 26px; border-radius: 50%; background: var(--brown); }
  .brand__name { font-size: 24px; font-weight: 700; color: var(--ink-dark); letter-spacing: .3px; }
  .title-band {
    position: absolute; left: 0; top: 303px; width: 100%; height: 152px;
    background:
      radial-gradient(ellipse 90% 60% at 50% 55%, var(--navy-deep) 30%, transparent 100%),
      linear-gradient(180deg, #0b3c7c 0%, #021d46 55%, #073275 100%);
  }
  .title-band__title {
    position: absolute; left: 51px; top: 23px;
    font-size: 26px; color: var(--white); font-weight: 400;
  }
  .title-band__subtitle {
    position: absolute; left: 51px; top: 66px;
    font-size: 19px; color: var(--white); font-weight: 400;
  }

  /* intro slide */
  .slide--intro .rule--top { top: 77px; height: 4px; }
  .slide-heading {
    position: absolute; left: 79px; top: 10px;
    font-size: 41px; font-weight: 400; color: var(--white);
  }
  .speaker__name {
    position: absolute; left: 72px; top: 145px;
    font-size: 29px; font-weight: 400; color: var(--ink-dark);
    text-shadow: 1px 1px 0 #c9c3bd, 2px 2px 2px rgba(0,0,0,.25);
  }
  .speaker__bio {
    position: absolute; left: 31px; top: 199px; width: 350px;
    font-size: 20px; line-height: 29.5px; color: var(--ink-blue);
  }
  .speaker__photo {
    position: absolute; left: 382px; top: 141px; width: 144px; height: 180px;
    border: 3px solid #0c0c0c;
    box-shadow: 2px 2px 3px rgba(0,0,0,.35);
    background: radial-gradient(ellipse at 50% 40%, #6f7c5c 0%, var(--photo-tone) 55%, #2f3a2d 100%);
  }
  .slide-footer {
    position: absolute; left: 0; bottom: 0; width: 100%; height: 37px;
    background: var(--footer-navy);
    border-top: 3px solid #16233a;
    color: var(--white); font-size: 10.5px;
  }
  .slide-footer span { position: absolute; top: 13px; }
  .slide-footer__date { left: 42px; }
  .slide-footer__text { left: 313px; }
  .slide-footer__page { right: 32px; }
</style>
</head>
<body>
  <section class="slide slide--title">
    <div class="header-art" role="img" aria-label="Abstract blue header with sweeping light arcs"></div>
    <div class="rule rule--top"></div>
    <div class="brand">
      <span class="brand__dot"></span>
      <span class="brand__name">Ironline Tax Co.</span>
    </div>
    <div class="rule rule--bottom"></div>
    <div class="title-band">
      <h1 class="title-band__title">Taxation for Real Estate Professionals</h1>
      <p class="title-band__subtitle">Sub Title</p>
    </div>
  </section>

  <section class="slide slide--intro">
    <div class="header-art" role="img" aria-label="Abstract blue header with sweeping light arcs"></div>
    <h2 class="slide-heading">Introductions</h2>
    <div class="rule rule--top"></div>
    <h3 class="speaker__name">Dale Porter, CPA</h3>
    <p class="speaker__bio">Member of the National Guild of Tax Resolution Advisors providing services for Accounting, Bookkeeping, Taxes, Consulting, and Training.</p>
    <div class="speaker__photo" role="img" aria-label="Portrait photo of the presenter"></div>
    <footer class="slide-footer">
      <span class="slide-footer__date">9/1/2016</span>
      <span class="slide-footer__text">Footer Text</span>
      <span class="slide-footer__page">Page#</span>
    </footer>
  </section>
</body>
</html>
```